Marlow Research, Inc. Site Design Project

Marlow Research, Inc is my private and small research office.
This naming shows:
We investigate every(*: asterisk) issue to support society.
We investigate "a star risk" which means every critical things for example, information security, branding, public communication - to understand for our clients - especially innovative person.
Last year, we had faced the great disaster in Japan, we investigated the damaged place, schools, and local governments, and supported communities like Quillfest Ogura.
So I want to get a high concept sites with good logo and to use card, website, and our letter.
Reason: We would like to look for more competitive candidates.
I uploaded the latest logo. If you have any idea to adapt it to your design, I appreciate it.
* marketing section of leading companies(enterprises)
* promotion agencies of government
* futurist and researcher
* business managers
Communication
for desirable future

```html
<!DOCTYPE html>
<html lang="en">
<head>
<meta charset="utf-8">
<title>Marlow Research, Inc</title>
<link rel="stylesheet" href="https://fonts.googleapis.com/css2?family=Arimo:ital,wght@0,400;0,700;1,400&family=Roboto+Condensed:wght@700&family=Tinos:wght@400;700&display=swap">
<style>
:root{
  --red:#d9171c;
  --red-dark:#b30f14;
  --red-light:#ee4b4f;
  --ink:#111;
  --grey:#8a8a8a;
  --page:#eeeeee;
  --card:#ffffff;
}
*{box-sizing:border-box;margin:0;padding:0}
html,body{width:1200px;height:1131px;overflow:hidden}
body{position:relative;background:var(--page);font-family:Arimo,Arial,sans-serif;color:var(--ink)}
.backdrop{position:absolute;inset:0 0 auto 0;height:720px;background:linear-gradient(180deg,#f4f4f4 0%,#c9c9c9 30%,#b8b8b8 50%,#e6e6e6 85%,var(--page) 100%)}
.card{position:absolute;left:143px;width:914px;background:var(--card);border:1px solid #9c9c9c;border-radius:4px;box-shadow:0 0 30px rgba(0,0,0,.18)}
.main{top:29px;height:835px;overflow:hidden}
.site-header{height:109px;position:relative}
.brand{position:absolute;left:20px;top:38px;display:flex;align-items:center;gap:10px}
.brand-mark{width:14px;height:14px;background:var(--red)}
.brand-name{font-family:Arimo,Arial,sans-serif;font-weight:700;font-size:26px;line-height:30px;color:var(--ink)}
.phone{position:absolute;right:20px;top:48px;display:flex;align-items:center;gap:4px;font-family:"Roboto Condensed",sans-serif;font-weight:700;font-size:29px}
.nav{height:41px;background:linear-gradient(180deg,var(--red-dark) 0%,var(--red) 45%,var(--red-light) 100%);display:flex;position:relative}
.nav a{display:block;text-align:center;color:#fff;text-decoration:none;font-family:Tinos,serif;font-weight:700;font-size:17px;line-height:41px;border-right:1px solid rgba(255,255,255,.35)}
.nav a:last-child{border-right:0}
.nav a.active{position:relative}
.nav a.active::after{content:"";position:absolute;left:50%;bottom:-8px;margin-left:-7px;border:7px solid transparent;border-top:8px solid var(--red-light);border-bottom:0}
.hero{height:333px;position:relative;background:linear-gradient(100deg,#1d8fd6 0%,#5ab3e6 30%,#a9d6ee 50%,#c98c78 70%,#e2a48e 100%)}
.hero h1{position:absolute;left:45px;top:66px;font-family:"Roboto Condensed",sans-serif;font-weight:700;font-size:35px;line-height:41px;color:#111}
.btn{display:inline-block;color:#fff;font-family:Tinos,serif;font-weight:700;background:linear-gradient(180deg,var(--red-light),var(--red));border:1px solid var(--red-dark);border-radius:4px}
.hero .btn{position:absolute;left:45px;top:159px;font-size:19px;padding:11px 13px}
.content{display:flex;padding:29px 19px 0 19px;gap:40px}
.welcome{width:590px}
.section-title{font-family:Tinos,serif;font-weight:700;font-size:24px;color:var(--red);padding-bottom:4px;border-bottom:3px double var(--red)}
.welcome p{font-size:12px;line-height:16.2px;margin-top:15px}
.welcome .section-title{margin-bottom:5px}
.welcome a{color:var(--red);font-weight:700;text-decoration:none}
.projects{width:248px;margin-top:-1px}
.project{display:flex;gap:9px;padding:18px 0 16px;border-bottom:1px dotted #555}
.project:last-child{border-bottom:0}
.thumb{width:58px;height:58px;border:1px solid #888;border-radius:3px;padding:3px;flex:none}
.thumb div{width:100%;height:100%}
.project h3{font-size:14px;line-height:16.5px;font-weight:700;margin-top:4px}
.project time{display:block;text-align:right;font-size:10px;font-style:italic;color:var(--grey);margin-top:3px}
.footer{top:879px;height:202px;display:flex;padding:26px 19px 0;gap:68px}
.col{width:248px}
.col h2{font-family:"Roboto Condensed",sans-serif;font-weight:700;font-size:17px;color:var(--red);border-bottom:1px solid #555;padding-bottom:1px;display:flex;justify-content:space-between;align-items:flex-end}
.col h2 small{font-family:Arimo,sans-serif;font-size:9px;font-style:italic}
.col p{font-size:12px;line-height:15.5px}
.quote{position:relative;padding:22px 0 0 8px}
.quote::before{content:"\201C";position:absolute;left:-4px;top:-2px;font-family:Tinos,serif;font-size:70px;color:#ddd;line-height:70px;z-index:0}
.quote p{position:relative}
.cite{text-align:right;font-size:10.5px;font-style:italic;line-height:13.5px;margin-top:12px}
.newsletter p{margin-top:16px}
.email{margin-top:10px;height:29px;border:1px solid #222;border-radius:2px;font-size:11px;font-style:italic;color:#999;padding:8px 7px}
.newsletter .btn{font-size:12px;padding:5px 6px;margin-top:8px}
.contact p{margin-top:14px}
.contact em{color:var(--red);font-size:9px;font-weight:700;margin-left:4px}
.social{display:flex;gap:2px;margin-top:3px}
.social span{width:14px;height:14px;border-radius:2px}
.copy{position:absolute;right:143px;top:1090px;font-family:Tinos,serif;font-size:12px;color:#999}
</style>
</head>
<body>
<div class="backdrop" role="img" aria-label="Faded black and white city skyline"></div>

<div class="card main">
  <header class="site-header">
    <div class="brand"><span class="brand-mark"></span><span class="brand-name">Marlow Research</span></div>
    <div class="phone">
      <svg width="30" height="26" viewBox="0 0 30 26"><rect x="1" y="3" width="13" height="22" rx="1.5" fill="#111"/><rect x="3.5" y="6" width="8" height="5" fill="#fff"/><g fill="#fff"><rect x="3.5" y="13" width="2" height="2"/><rect x="6.5" y="13" width="2" height="2"/><rect x="9.5" y="13" width="2" height="2"/><rect x="3.5" y="17" width="2" height="2"/><rect x="6.5" y="17" width="2" height="2"/><rect x="9.5" y="17" width="2" height="2"/></g><g fill="none" stroke="#111" stroke-width="1.6"><path d="M17 4a5 5 0 0 1 0 7"/><path d="M20 1.5a9 9 0 0 1 0 12"/><path d="M23 -1a13 13 0 0 1 0 17"/></g></svg>
      03.5550.2418
    </div>
  </header>
  <nav class="nav">
    <a class="active" style="width:126px">*Home</a>
    <a style="width:151px">*About Us</a>
    <a style="width:141px">*Services</a>
    <a style="width:142px">*Projects</a>
    <a style="width:187px">*Press Releases</a>
    <a style="width:167px">*Contact Us</a>
  </nav>
  <section class="hero" role="img" aria-label="Close-up of a researcher in glasses reading a bright screen">
    <h1>LATEST REPORT FROM<br>MARLOW RESEARCH, INC</h1>
    <span class="btn">*Learn What We Can Do</span>
  </section>
  <div class="content">
    <section class="welcome">
      <h2 class="section-title">*Welcome to Marlow Research, Inc</h2>
      <p>Lorem ipsum dolor sit amet, consectetur adipiscing elit. Praesent fermentum lacus non leo vestibulum venenatis. Nam at sodales dolor. Maecenas condimentum dictum odio non iaculis. Aenean neque diam, porta auctor euismod eu, viverra quis nisi. Sed dapibus nisl sit amet risus auctor in tempor diam rhoncus. Donec quis nisi leo. Morbi dignissim congue ligula, id porttitor nulla. Donec a elit sem. Pellentesque et nulla ut quam auctor aliquet. Etiam at ipsum eu erat fermentum.</p>
      <p>Mauris laoreet sem quis nulla eleifend auctor malesuada dolor pellentesque. Cras accumsan rutrum magna. Class aptent taciti sociosqu ad litora torquent per conubia nostra, per inceptos himenaeos. Vestibulum elementum, neque vitae convallis faucibus, elit leo vulputate sapien, vel imperdiet felis lorem a enim. Nulla facilisi. Phasellus vel urna at diam consectetur laoreet pulvinar at quam. Sed mauris felis, congue quis dignissim sed, rutrum a justo vivamusporta volutpat ullamcorper a urna. Phasellus erat sem, eleifend in egestas in, aliquam a nibh <a>contact us</a>.</p>
    </section>
    <aside class="projects">
      <h2 class="section-title">*Recent Projects</h2>
      <article class="project">
        <div class="thumb"><div role="img" aria-label="Business handshake" style="background:linear-gradient(160deg,#2a5ea8,#9ab8d8)"></div></div>
        <div><h3>Lorem ipsum dolor sit amet, consectetur elit.</h3><time>10 June, 2012</time></div>
      </article>
      <article class="project">
        <div class="thumb"><div role="img" aria-label="Blue charts and graphs" style="background:linear-gradient(160deg,#1a3f9e,#7fa6e0)"></div></div>
        <div><h3>Lorem ipsum dolor sit amet, consectetur elit.</h3><time>9 June, 2012</time></div>
      </article>
      <article class="project">
        <div class="thumb"><div role="img" aria-label="Person with raised arms against the sky" style="background:linear-gradient(180deg,#3d8fd6,#bcdcf2)"></div></div>
        <div><h3>Lorem ipsum dolor sit amet, consectetur elit.</h3><time>8 June, 2012</time></div>
      </article>
    </aside>
  </div>
</div>

<footer class="card footer">
  <section class="col">
    <h2>TESTIMONIALS <small>View All &gt;</small></h2>
    <div class="quote"><p>Lorem ipsum dolor sit amet, consectetur adipiscing elit. Mauris eleifend ultrices tincidunt. Curabitur malesuada tincidunt turpis, luctus tincidunt lectus tristique sed. Curabitur dictum enim turpis, cursus.</p></div>
    <p class="cite">Nadia Ferrant<br>Bluefern Capital Partners</p>
  </section>
  <section class="col newsletter">
    <h2>NEWSLETTER</h2>
    <p>Lorem ipsum dolor sit amet, consectetur adip iscing elit eleifend ultrices tincidunt.</p>
    <div class="email">Please Enter Your Email</div>
    <span class="btn">*Submit</span>
  </section>
  <section class="col contact">
    <h2>MARLOW RESEARCH, INC.</h2>
    <p>7-4 Kanda<br>Chiyoda-ku<br>Tokyo 101-0044 Japan <em>Directions &gt;</em></p>
    <p>Ph: 03.5550.2418<br>Email: info@MarlowResearch.com</p>
    <div class="social"><span style="background:#3b5998"></span><span style="background:#3aa9e0"></span><span style="background:#1c7bb5"></span><span style="background:#f08a1c"></span></div>
  </section>
</footer>

<p class="copy">©2012 Marlow Research, Inc.</p>
</body>
</html>
```